Indonesian B2B Company (Varo Ingredients) - Stationery Design

Varo Ingredients needs a corporate, bold and professional-looking stationery design.

Varo Ingredients is a new Indonesian company manufacturing, marketing and distributing various ingredients / raw materials such as flavours, fragrance, colours, sweeteners, preservatives for the food & beverage, pharmaceutical, personal care and other household goods industries.

It is a business to business (B2B) company as we supply various natural and synthetic raw materials to various consumer goods manufacturers. We therefore need a logo/identity with corporate and industrial style.

Varo Ingredients is a startup company which belongs to a larger Varo Tunggal group of companies (http://varotunggal.dealpathway.com/about) that focuses in the mining, petroleum and energy businesses. Varo Ingredients would like to focus in providing good quality, safe, reliable and affordable ingredients for the industries. Our tagline is "Quality Materials, Reliable Supply"
Updates

We have updated some information including our requirements and contact details to be shown in the stationery. Please check the project brief.

Regards,

Varo Ingredients

Target Market(s)

Manufacturers of food & beverages, personal care, pharmaceutical and other FMCG factories.

Industry/Entity Type

Business

Requirements
Must have
• Smart, professional and corporate touches in the stationery designs. We require designs for:
1. Letterhead
2. Envelope (with and without window)
3. Name card
4. Powerpoint presentation template
5. CD label
6. Small memo / with compliments card

Contact details:

Company name:
PT Varo Ingredients

Address:
Ruko Melati Sentosa Utara, Blok K07 no: 15-16
Duren Sawit Selatan, 13470
Indonesia

Tel:+62 21 738 2906
Fax:+62 21 738 2907
Email: info@varo-ingredients.co.id
Website: www.varo-ingredients.co.id

```html
<!DOCTYPE html>
<html lang="en">
<head>
<meta charset="utf-8">
<title>Varo Ingredients – Stationery Set</title>
<link rel="stylesheet" href="https://fonts.googleapis.com/css2?family=Titillium+Web:wght@400;600&display=swap">
<style>
  :root {
    --brand-red: #e2231a;
    --ink: #3a3a3a;
    --muted: #8a8a8a;
    --paper: #ffffff;
    --backdrop: #e9e7e3;
    --rule-grey: #d6d6d6;
  }
  * { box-sizing: border-box; margin: 0; padding: 0; }
  html, body { width: 1200px; height: 900px; overflow: hidden; }
  body {
    background: var(--backdrop);
    font-family: "Titillium Web", Arial, sans-serif;
    color: var(--ink);
    position: relative;
  }
  address { font-style: normal; }
  .sheet {
    position: absolute;
    background: var(--paper);
    box-shadow: 0 2px 6px rgba(0,0,0,.18);
  }
  .brand-name {
    display: flex; align-items: center; gap: .4em;
    color: var(--ink);
    font-weight: 600;
    line-height: 1;
    white-space: nowrap;
  }
  .brand-name::before {
    content: ""; width: .6em; height: .6em; background: var(--brand-red); flex: none;
  }
  .brand-tagline { color: var(--muted); font-weight: 400; white-space: nowrap; }
  .company { color: var(--brand-red); font-weight: 600; }

  /* Letterhead */
  .letterhead { left: 50px; top: 102px; width: 495px; height: 700px; }
  .letterhead .brand { position: absolute; left: 30px; top: 58px; }
  .letterhead .brand-name { font-size: 19px; }
  .letterhead .brand-tagline { font-size: 9px; margin-top: 4px; }
  .letterhead .sender {
    position: absolute; right: 20px; top: 16px; text-align: right;
    font-size: 8px; line-height: 11px;
  }
  .letterhead .sender .company { font-size: 9px; margin-bottom: 10px; }
  .letterhead .sender .gap { height: 11px; }
  .letterhead .edge-bar {
    position: absolute; right: 0; top: 84px; width: 4px; height: 36px; background: var(--brand-red);
  }
  .letterhead .site {
    position: absolute; right: 20px; bottom: 10px; font-size: 8px; letter-spacing: 2px; color: var(--muted);
  }

  /* Business cards */
  .card { width: 208px; height: 117px; border-radius: 9px; overflow: hidden; }
  .card-front { left: 650px; top: 123px; }
  .card-back { left: 874px; top: 123px; }
  .card-front .holder { position: absolute; left: 12px; top: 8px; width: 90px; }
  .card-front .holder-name { color: var(--brand-red); font-weight: 600; font-size: 7px; line-height: 8px; }
  .card-front .company { font-size: 5px; line-height: 6px; margin-top: 4px; }
  .card-front .details { font-size: 4.5px; line-height: 6px; color: var(--muted); }
  .contact-list { list-style: none; margin-top: 3px; font-size: 4.5px; line-height: 6px; color: var(--muted); }
  .contact-list li::before {
    content: ""; display: inline-block; width: 3px; height: 3px; background: var(--brand-red); margin-right: 4px;
  }
  .card-front .brand { position: absolute; left: 108px; top: 48px; }
  .card-front .brand-name { font-size: 11px; }
  .card-front .brand-tagline { font-size: 5px; margin-top: 2px; }
  .card-back .brand { position: absolute; left: 0; right: 0; top: 46px; display: flex; flex-direction: column; align-items: center; }
  .card-back .brand-name { font-size: 13px; }
  .card-back .brand-tagline { font-size: 6px; margin-top: 2px; }
  .card-back .site {
    position: absolute; left: 0; right: 0; bottom: 8px; text-align: center;
    font-size: 5px; letter-spacing: 1.5px; color: var(--muted);
  }

  /* Compliment slip */
  .compliment-slip { left: 583px; top: 270px; width: 566px; height: 248px; }
  .compliment-slip .brand { position: absolute; left: 35px; top: 86px; }
  .compliment-slip .brand-name { font-size: 17px; }
  .compliment-slip .brand-tagline { font-size: 8px; margin-top: 4px; }
  .compliment-slip .sender { position: absolute; left: 33px; top: 128px; font-size: 8px; line-height: 11px; }
  .compliment-slip .sender .company { font-size: 9px; margin-bottom: 10px; }

  /* Envelope */
  .envelope { left: 583px; top: 537px; width: 566px; height: 246px; }
  .envelope .flap { position: absolute; inset: 0; }
  .envelope .brand { position: absolute; left: 0; right: 0; top: 38px; display: flex; justify-content: center; }
  .envelope .brand-name { font-size: 15px; }
  .envelope .return {
    position: absolute; left: 0; right: 0; top: 190px; text-align: center; font-size: 8px; line-height: 11px;
  }
  .envelope .accent-line {
    width: 170px; height: 2px; margin: 0 auto 4px;
    background: linear-gradient(90deg, transparent, var(--brand-red), transparent);
  }
  .envelope .company { font-size: 9px; }
</style>
</head>
<body>

<section class="sheet letterhead">
  <div class="brand">
    <div class="brand-name">Varo Ingredients</div>
    <div class="brand-tagline">Quality Materials, Reliable Supply</div>
  </div>
  <address class="sender">
    <div class="company">PT Varo Ingredients</div>
    Ruko Melati Sentosa Utara<br>
    Blok K07 no: 15-16<br>
    Duren Sawit Selatan, 13470<br>
    Indonesia
    <div class="gap"></div>
    Tel:+62 21 738 2906<br>
    Fax:+62 21 738 2907<br>
    Email: info@varo-ingredients.co.id
  </address>
  <div class="edge-bar"></div>
  <div class="site">www.varo-ingredients.co.id</div>
</section>

<section class="sheet card card-front">
  <div class="holder">
    <div class="holder-name">Dimas Prakoso</div>
    <div class="details">Managing Director</div>
    <ul class="contact-list">
      <li>+62 21 738 2906</li>
      <li>info@varo-ingredients.co.id</li>
    </ul>
    <div class="company">PT Varo Ingredients</div>
    <div class="details">Ruko Melati Sentosa Utara<br>Blok K07 no: 15-16<br>Duren Sawit Selatan, 13470<br>Indonesia</div>
    <ul class="contact-list">
      <li>+62 21 738 2906</li>
      <li>+62 21 738 2907</li>
      <li>www.varo-ingredients.co.id</li>
    </ul>
  </div>
  <div class="brand">
    <div class="brand-name">Varo Ingredients</div>
    <div class="brand-tagline">Quality Materials, Reliable Supply</div>
  </div>
</section>

<section class="sheet card card-back">
  <div class="brand">
    <div class="brand-name">Varo Ingredients</div>
    <div class="brand-tagline">Quality Materials, Reliable Supply</div>
  </div>
  <div class="site">www.varo-ingredients.co.id</div>
</section>

<section class="sheet compliment-slip">
  <div class="brand">
    <div class="brand-name">Varo Ingredients</div>
    <div class="brand-tagline">Quality Materials, Reliable Supply</div>
  </div>
  <address class="sender">
    <div class="company">PT Varo Ingredients</div>
    Ruko Melati Sentosa Utara<br>
    Blok K07 no: 15-16<br>
    Duren Sawit Selatan, 13470<br>
    Indonesia
  </address>
</section>

<section class="sheet envelope">
  <svg class="flap" width="566" height="246" viewBox="0 0 566 246" aria-hidden="true">
    <path d="M0 0 L255 108 Q283 118 311 108 L566 0" fill="none" stroke="var(--rule-grey)" stroke-width="1"/>
    <path d="M0 246 L180 120 M566 246 L386 120" fill="none" stroke="var(--rule-grey)" stroke-width="1"/>
  </svg>
  <div class="brand">
    <div class="brand-name">Varo Ingredients</div>
  </div>
  <address class="return">
    <div class="accent-line"></div>
    <div class="company">PT Varo Ingredients</div>
    Ruko Melati Sentosa Utara, Blok K07 no: 15-16 Duren Sawit Selatan, 13470 Indonesia<br>
    Tel:+62 21 738 2906 &nbsp;Fax:+62 21 738 2907 &nbsp;Email: info@varo-ingredients.co.id
  </address>
</section>

</body>
</html>
```